DOUBLE SIDED BROCHURE NEEDED TO PROMOTE DOCTOR

I need a double sided DL size (99mm x 210mm) brochure, promoting a doctor seeing patients in a new area.

I want something professional. I have included the relevant information. I would also like the Dr's picture somwhere in the brochure, with a professional background. I wish to print these tomorrow, so i will pick a winner within 14 hours of posting this ad.

I have included an example of a brochures design that I recently saw, and its definietly a good starting point.

Medical

```html
<!DOCTYPE html>
<html lang="en">
<head>
<meta charset="utf-8">
<title>Dr. Haddad – Referral Brochure</title>
<link rel="stylesheet" href="https://fonts.googleapis.com/css2?family=Exo+2:wght@500;600;700;800&family=Arimo:wght@400;700&display=swap">
<style>
  :root {
    --teal-light: #6fd0dc;
    --teal: #33a9ba;
    --teal-deep: #1f8595;
    --ink: #17252e;
    --grey-light: #f3f4f4;
    --grey: #d7dadb;
    --page: #ececec;
    --white: #ffffff;
  }
  * { box-sizing: border-box; margin: 0; padding: 0; }
  html, body { width: 1200px; height: 1192px; overflow: hidden; }
  body {
    background: var(--page);
    font-family: "Arimo", Arial, sans-serif;
    color: var(--ink);
    position: relative;
  }
  .panel {
    position: absolute;
    top: 90px;
    width: 470px;
    height: 1010px;
    overflow: hidden;
    background: linear-gradient(180deg, var(--grey-light), var(--grey));
    box-shadow: 0 6px 22px rgba(0,0,0,0.18);
  }
  .panel--front { left: 95px; }
  .panel--back { left: 635px; }
  .layer { position: absolute; left: 0; width: 100%; }
  .layer > svg { position: absolute; inset: 0; }
  .heading {
    font-family: "Exo 2", sans-serif;
    font-weight: 700;
    color: var(--white);
  }
  .icon { width: 15px; height: 15px; fill: currentColor; vertical-align: -2px; margin-right: 6px; }

  /* Front */
  .front-photo {
    top: 280px; height: 470px;
    background: linear-gradient(160deg, #dfeef3 0%, #b5d3de 45%, #6e9fb3 75%, #c9d8de 100%);
  }
  .front-header { top: 0; height: 340px; }
  .front-intro { position: absolute; top: 28px; left: 26px; right: 26px; }
  .front-intro .heading { font-size: 26px; margin-bottom: 18px; }
  .front-intro p { font-size: 15px; line-height: 1.36; margin-bottom: 18px; }
  .front-intro strong { font-weight: 700; }
  .front-footer { top: 680px; height: 330px; }
  .contact-tab {
    position: absolute; top: 96px; left: 0;
    background: var(--teal-deep);
    color: var(--white);
    font-family: "Exo 2", sans-serif; font-weight: 700;
    font-size: 18px; letter-spacing: 0.3px;
    padding: 8px 16px 8px 22px;
    border-radius: 0 8px 8px 0;
  }
  .contact-list { position: absolute; top: 148px; left: 22px; font-size: 15.5px; line-height: 1.28; }
  .contact-label { color: var(--teal-deep); font-weight: 700; }
  .contact-label--gap { margin-top: 4px; }
  .contact-label--fax { font-size: 14.5px; }
  .badge { position: absolute; top: 84px; left: 285px; width: 170px; height: 170px; }
  .badge svg { position: absolute; inset: 0; }
  .badge-text {
    position: absolute; inset: 0;
    display: flex; flex-direction: column; align-items: center; justify-content: center;
    text-align: center; font-family: "Exo 2", sans-serif; line-height: 1.05;
  }
  .badge-top { font-size: 19px; font-weight: 800; color: var(--white); }
  .badge-mid { font-size: 12px; color: var(--ink); margin: 3px 0; }
  .badge-bottom { font-size: 18px; font-weight: 800; color: var(--ink); }

  /* Back */
  .back-header { top: 0; height: 270px; }
  .back-intro { position: absolute; top: 24px; left: 26px; right: 24px; }
  .back-intro .heading { font-size: 23px; line-height: 1.28; }
  .back-intro p { margin-top: 18px; font-size: 16px; line-height: 1.35; }
  .services { position: absolute; left: 26px; right: 20px; list-style: none; font-size: 15.5px; line-height: 1.35; }
  .services li { position: relative; padding-left: 20px; margin-bottom: 7px; }
  .services li::before {
    content: ""; position: absolute; left: 0; top: 6px;
    width: 8px; height: 8px; border-radius: 50%; background: var(--teal);
  }
  .services .sub { display: block; }
  .services--specialist { top: 295px; }
  .services--general { top: 560px; }
  .services-heading {
    position: absolute; top: 515px; left: 26px;
    font-family: "Exo 2", sans-serif; font-weight: 700; font-size: 19px; color: var(--teal);
  }
  .back-footer { top: 690px; height: 320px; }
  .back-contact { position: absolute; top: 108px; left: 24px; font-size: 15.5px; line-height: 1.3; }
  .back-contact .clinic { color: var(--white); font-size: 16px; }
  .back-contact .indent { padding-left: 21px; }
  .back-contact .spaced { margin-top: 16px; }
  .back-contact .note { color: var(--white); font-size: 11.5px; margin-top: 16px; }
  .portrait {
    position: absolute; top: 660px; left: 255px; width: 215px; height: 350px;
    background: linear-gradient(170deg, #bfc5c9 0%, #8b949b 40%, #2f3a4a 75%, #1e2633 100%);
    border-radius: 40px 0 0 0;
  }
</style>
</head>
<body>
<svg width="0" height="0" style="position:absolute" aria-hidden="true">
  <defs>
    <symbol id="icon-pin" viewBox="0 0 16 16"><path d="M8 0a5.5 5.5 0 0 0-5.5 5.5C2.5 9.6 8 16 8 16s5.5-6.4 5.5-10.5A5.5 5.5 0 0 0 8 0zm0 7.8a2.3 2.3 0 1 1 0-4.6 2.3 2.3 0 0 1 0 4.6z"/></symbol>
    <symbol id="icon-phone" viewBox="0 0 16 16"><path d="M3.6 1 6 3.4 4.7 5.6a9 9 0 0 0 5.7 5.7l2.2-1.3L15 12.4 13.3 15C6.8 14.6 1.4 9.2 1 2.7z"/></symbol>
    <symbol id="icon-fax" viewBox="0 0 16 16"><path d="M4 1h7l1 1v3H4zM1 6h14v7h-2v2H3v-2H1zm4 5v3h6v-3z"/></symbol>
    <linearGradient id="teal-fill" x1="0" y1="0" x2="0" y2="1">
      <stop offset="0" stop-color="#72d3de"/><stop offset="1" stop-color="#2fa4b5"/>
    </linearGradient>
  </defs>
</svg>

<!-- Front panel -->
<section class="panel panel--front">
  <div class="layer front-photo" role="img" aria-label="Photo of a stethoscope resting on medical notes on a clinic desk"></div>

  <div class="layer front-header">
    <svg width="470" height="340" viewBox="0 0 470 340" preserveAspectRatio="none">
      <path d="M0 0H470V290C360 330 230 270 0 320Z" fill="url(#teal-fill)"/>
      <path d="M0 326C220 274 360 336 470 296" fill="none" stroke="#ffffff" stroke-width="5" opacity="0.85"/>
    </svg>
    <div class="front-intro">
      <h1 class="heading">Dear Doctors,</h1>
      <p>We are pleased to announce that <strong>Dr.Karim Haddad</strong> is now consulting in Seacliff, seeing public and private patients.</p>
      <p>Guaranteed appointment within two weeks, with patients having the option of surgery at Coastal Health Campus, Riverside General Hospital or St. Anne's Southbank.</p>
    </div>
  </div>

  <div class="layer front-footer">
    <svg width="470" height="330" viewBox="0 0 470 330" preserveAspectRatio="none">
      <path d="M0 40C150 0 300 80 470 20V330H0Z" fill="#2a95a5"/>
      <path d="M0 70C170 30 300 100 470 50V330H0Z" fill="#e9ebeb"/>
    </svg>
    <div class="contact-tab">CONTACT DETAILS:</div>
    <div class="contact-list">
      <div class="contact-label"><svg class="icon"><use href="#icon-pin"/></svg>Seacliff Clinic:</div>
      <div>48 Harbourside Drive</div>
      <div>Seacliff WA 6190</div>
      <div class="contact-label contact-label--gap"><svg class="icon"><use href="#icon-phone"/></svg>Phone:</div>
      <div>1300 482 071</div>
      <div class="contact-label contact-label--fax"><svg class="icon"><use href="#icon-fax"/></svg>Please send all referrals by fax to</div>
      <div>(08) 6204 3385</div>
    </div>
    <div class="badge">
      <svg viewBox="0 0 170 170" width="170" height="170">
        <polygon fill="#33a9ba" points="170,85 157.6,99.4 163.5,117.6 146.5,126.1 145.1,145.1 126.1,146.5 117.6,163.5 99.4,157.6 85,170 70.6,157.6 52.4,163.5 43.9,146.5 24.9,145.1 23.5,126.1 6.5,117.6 12.4,99.4 0,85 12.4,70.6 6.5,52.4 23.5,43.9 24.9,24.9 43.9,23.5 52.4,6.5 70.6,12.4 85,0 99.4,12.4 117.6,6.5 126.1,23.5 145.1,24.9 146.5,43.9 163.5,52.4 157.6,70.6"/>
        <circle cx="85" cy="85" r="66" fill="none" stroke="#ffffff" stroke-width="2" opacity="0.7"/>
      </svg>
      <div class="badge-text">
        <span class="badge-top">GUARANTEED</span>
        <span class="badge-mid">appointment within</span>
        <span class="badge-bottom">TWO WEEKS</span>
      </div>
    </div>
  </div>
</section>

<!-- Back panel -->
<section class="panel panel--back">
  <div class="layer back-header">
    <svg width="470" height="270" viewBox="0 0 470 270" preserveAspectRatio="none">
      <path d="M0 0H470V200C350 260 180 190 0 240Z" fill="url(#teal-fill)"/>
      <path d="M0 250C180 200 340 266 470 210" fill="none" stroke="#2a95a5" stroke-width="4"/>
    </svg>
    <div class="back-intro">
      <h2 class="heading">Dr.Haddad is a highly trained specialised surgeon.</h2>
      <p>in all areas of Endocrine, Breast and General Surgery. Including;</p>
    </div>
  </div>

  <ul class="services services--specialist">
    <li>Thyroid Surgery</li>
    <li>Parathyroid surgery <span class="sub">(including minimally invasive parathyroidectomy)</span></li>
    <li>Breast Cancer <span class="sub">Benign breast lesions</span></li>
  </ul>

  <h3 class="services-heading">All areas of general surgery, such as:</h3>
  <ul class="services services--general">
    <li>Gallbladder surgery</li>
    <li>Hernia surgery</li>
    <li>Haemorrhoids</li>
    <li>Carpal Tunnel</li>
    <li>Vasectomy etc etc…</li>
  </ul>

  <div class="layer back-footer">
    <svg width="470" height="320" viewBox="0 0 470 320" preserveAspectRatio="none">
      <path d="M0 50C160 0 300 90 470 30V320H0Z" fill="#2a95a5"/>
      <path d="M0 80C170 35 310 110 470 60V320H0Z" fill="url(#teal-fill)"/>
    </svg>
    <div class="back-contact">
      <div class="clinic">Seacliff Clinic:</div>
      <div><svg class="icon"><use href="#icon-pin"/></svg>48 Harbourside Drive</div>
      <div class="indent">Seacliff WA 6190</div>
      <div class="spaced"><svg class="icon"><use href="#icon-phone"/></svg>1300 482 071</div>
      <div class="note">Please send all referrals by fax to</div>
      <div><svg class="icon"><use href="#icon-fax"/></svg>(08) 6204 3385</div>
    </div>
  </div>

  <div class="portrait" role="img" aria-label="Portrait of Dr. Haddad in a dark suit against a professional backdrop"></div>
</section>
</body>
</html>
```